Business Card - connecting 2 souls and beggining the journey of self discovery

Logo on the front
with tag line

On the back list of services and contact details

Seminars
workshops
Coaching
podcasts

Daniel Porthwick
Health & Wellbeing Life Coach
0491 372 815
daniel@wovenpathwellness.example
wovenpathwellness.example

Industry/Entity Type

Life Coaching

Contact Information for Business Card

I like the use of colour from the logo to be used. I'm not a fan of white.

Requirements
Must have
• My tagline: The journey home starts with you
Nice to have
• Use of colour that is in the mind body soul logo

```html
<!DOCTYPE html>
<html lang="en">
<head>
<meta charset="utf-8">
<title>Woven Path Wellness – Business Card</title>
<link rel="stylesheet" href="https://fonts.googleapis.com/css2?family=Caveat:wght@500&family=Montserrat:wght@600&family=Open+Sans:ital,wght@0,400;0,600;1,400&family=Quicksand:wght@500;700&display=swap">
<style>
  :root {
    --page: #ffffff;
    --guide: #9a9a9a;
    --card-white: #ffffff;
    --teal: #3aa59a;
    --teal-deep: #2f9c95;
    --green: #7cbf4a;
    --yellow: #f2c530;
    --gold: #e9b52c;
    --orange: #ef8a3c;
    --coral: #e0595e;
    --purple: #7a3c96;
    --brand-grey: #808084;
    --ink-white: #ffffff;
  }
  * { margin: 0; padding: 0; box-sizing: border-box; }
  html, body {
    width: 692px; height: 1200px; overflow: hidden;
    background: var(--page);
  }
  .canvas { position: relative; width: 692px; height: 1200px; }

  /* dimension guides */
  .dim-width {
    position: absolute; left: 70px; top: 318px; width: 290px;
    display: flex; align-items: center; gap: 12px;
    font: italic 400 20px "Open Sans", sans-serif; color: var(--guide);
  }
  .dim-width::before, .dim-width::after {
    content: ""; flex: 1; height: 1px; background: var(--guide);
  }
  .dim-height {
    position: absolute; left: 14px; top: 360px; width: 48px; height: 464px;
    font: italic 400 20px "Open Sans", sans-serif; color: var(--guide);
  }
  .dim-height::before {
    content: ""; position: absolute; left: 47px; top: 0; width: 1px; height: 100%;
    background: var(--guide);
  }
  .dim-height span {
    position: absolute; top: 50%; left: 0; transform: translateY(-50%);
    background: var(--page); padding: 6px 0; white-space: nowrap;
    margin-left: -6px;
  }
  .side-label {
    position: absolute; top: 836px;
    font: italic 400 20px "Open Sans", sans-serif; color: var(--guide);
  }
  .side-label.front { left: 302px; }
  .side-label.back { left: 618px; }

  /* cards */
  .card {
    position: absolute; top: 360px; width: 290px; height: 464px; overflow: hidden;
  }
  .card-front {
    left: 70px; background: var(--card-white);
    outline: 1px solid #b5b5b5;
    display: flex; flex-direction: column; align-items: center;
  }
  .tagline {
    margin-top: 26px; text-align: center;
    font: 500 31px/1.05 "Caveat", cursive; color: var(--teal);
  }
  .brand-dot {
    margin-top: 36px; width: 150px; height: 150px; border-radius: 50%;
    background: var(--teal);
  }
  .brand-name {
    margin-top: 30px; text-align: center;
    font: 600 33px/1.05 "Montserrat", sans-serif; color: var(--brand-grey);
    letter-spacing: -0.5px;
  }

  .card-back { left: 382px; }
  .card-back svg { display: block; }
  .name-first { font: 500 30px "Quicksand", sans-serif; fill: var(--ink-white); }
  .name-last { font: 700 38px "Quicksand", sans-serif; fill: var(--ink-white); }
  .role { font: 400 15.5px "Open Sans", sans-serif; fill: var(--ink-white); }
  .service-outer { font: 600 28px "Open Sans", sans-serif; fill: var(--purple); letter-spacing: 0.5px; }
  .service-inner { font: 600 18px "Open Sans", sans-serif; fill: var(--ink-white); letter-spacing: 0.3px; }
  .contact-small { font: 400 9px "Open Sans", sans-serif; fill: var(--ink-white); }
  .contact-phone { font: 600 17px "Open Sans", sans-serif; fill: var(--purple); letter-spacing: 1px; }
</style>
</head>
<body>
<main class="canvas">
  <div class="dim-width">50 mm</div>
  <div class="dim-height"><span>80 mm</span></div>

  <section class="card card-front" aria-label="Card front">
    <p class="tagline">The journey home<br>starts with you</p>
    <div class="brand-dot" aria-hidden="true"></div>
    <h1 class="brand-name">Woven<br>Path<br>Wellness</h1>
  </section>

  <section class="card card-back" aria-label="Card back">
    <svg width="290" height="464" viewBox="0 0 290 464" xmlns="http://www.w3.org/2000/svg">
      <defs>
        <linearGradient id="back-bg" x1="0" y1="0" x2="0" y2="1">
          <stop offset="0" stop-color="var(--teal-deep)"/>
          <stop offset="0.55" stop-color="#5fb46a"/>
          <stop offset="1" stop-color="var(--green)"/>
        </linearGradient>
        <linearGradient id="warm-disc" x1="0" y1="0" x2="1" y2="1">
          <stop offset="0" stop-color="var(--gold)"/>
          <stop offset="0.5" stop-color="var(--yellow)"/>
          <stop offset="1" stop-color="var(--orange)"/>
        </linearGradient>
        <linearGradient id="service-ring" x1="0" y1="0" x2="1" y2="1">
          <stop offset="0" stop-color="var(--purple)"/>
          <stop offset="0.5" stop-color="var(--coral)"/>
          <stop offset="1" stop-color="var(--orange)"/>
        </linearGradient>
        <!-- circles around (145,293), starting at 12 o'clock, clockwise, drawn twice -->
        <path id="ring-112" d="M145,181 A112,112 0 1 1 145,405 A112,112 0 1 1 145,181 A112,112 0 1 1 145,405 A112,112 0 1 1 145,181"/>
        <path id="ring-108" d="M145,185 A108,108 0 1 1 145,401 A108,108 0 1 1 145,185 A108,108 0 1 1 145,401 A108,108 0 1 1 145,185"/>
        <path id="ring-70" d="M145,223 A70,70 0 1 1 145,363 A70,70 0 1 1 145,223 A70,70 0 1 1 145,363 A70,70 0 1 1 145,223"/>
      </defs>

      <rect class="back-field" width="290" height="464" fill="url(#back-bg)"/>
      <path class="corner-swell" d="M290,250 C245,240 240,330 255,390 C265,430 290,445 290,445 Z" fill="var(--green)" opacity="0.85"/>
      <circle class="warm-disc" cx="145" cy="293" r="160" fill="url(#warm-disc)"/>
      <path class="coral-swell" d="M0,380 C25,430 60,470 110,464 L0,464 Z" fill="var(--coral)" opacity="0.75"/>
      <circle class="service-ring" cx="145" cy="293" r="92" fill="url(#service-ring)"/>
      <circle class="core" cx="145" cy="293" r="52" fill="var(--green)"/>

      <text class="name-first" x="145" y="44" text-anchor="middle">Daniel</text>
      <text class="name-last" x="150" y="86" text-anchor="middle">Porthwick</text>
      <rect class="name-rule" x="26" y="96" width="214" height="3" fill="var(--yellow)"/>
      <text class="role" x="145" y="122" text-anchor="middle">Health &amp; Wellbeing Life Coach</text>

      <text class="service-outer"><textPath href="#ring-112" startOffset="50%" text-anchor="middle">COACHING</textPath></text>
      <text class="service-inner"><textPath href="#ring-70" startOffset="47.2%" text-anchor="middle">SEMINARS</textPath></text>
      <text class="service-inner"><textPath href="#ring-70" startOffset="61.8%" text-anchor="middle">PODCAST</textPath></text>
      <text class="service-inner"><textPath href="#ring-70" startOffset="81.3%" text-anchor="middle">WORKSHOPS</textPath></text>

      <text class="contact-small"><textPath href="#ring-108" startOffset="63.5%" text-anchor="middle">daniel@wovenpathwellness.example</textPath></text>
      <text class="contact-phone"><textPath href="#ring-112" startOffset="77.1%" text-anchor="middle">0491 372 815</textPath></text>
      <text class="contact-small"><textPath href="#ring-108" startOffset="90%" text-anchor="middle">wovenpathwellness.example</textPath></text>
    </svg>
  </section>

  <span class="side-label front">Front</span>
  <span class="side-label back">Back</span>
</main>
</body>
</html>
```